Have photos and logo just need help with web banner

Dimensions: 950 width by 425 height, pixels
Resolution: 92 DPI
Layout: Landscape
Format: JPG

Target Market(s)

Luxury market for women 28-55

Industry/Entity Type

Landscape

Number of Pages Required

1 page

Font styles to use
Script

Requirements
Must have
• Elegant, sophisticated feel
• Tagline: bags with a silver lining
Nice to have
• Shoes bag / has athletic, strong feel
Should not have
• Not cluttered. Not confusing.

```html
<!DOCTYPE html>
<html lang="en">
<head>
<meta charset="utf-8">
<title>Mirelle Web Banner</title>
<link rel="stylesheet" href="https://fonts.googleapis.com/css2?family=Great+Vibes&family=Open+Sans:wght@400;600&display=swap">
<style>
  :root {
    --paper: #ffffff;
    --band-grey: #6b6b6b;
    --brand-grey: #666666;
    --photo-dark: #2a2a2a;
    --photo-mid: #6d6d6b;
    --photo-light: #b9b8b3;
    --text-light: #ffffff;
  }
  html, body {
    margin: 0;
    padding: 0;
    overflow: hidden;
    background: var(--paper);
  }
  .banner {
    position: relative;
    width: 1200px;
    height: 537px;
    overflow: hidden;
    background: var(--paper);
  }
  .banner__shapes {
    position: absolute;
    inset: 0;
    width: 1200px;
    height: 537px;
  }
  .brand {
    position: absolute;
    left: 120px;
    top: 196px;
    width: 240px;
    text-align: center;
    font-family: "Open Sans", sans-serif;
    font-weight: 400;
    font-size: 30px;
    letter-spacing: 0.32em;
    color: var(--brand-grey);
    text-transform: uppercase;
  }
  .promo {
    position: absolute;
    right: 70px;
    top: 302px;
    text-align: right;
    color: var(--text-light);
  }
  .promo__title {
    margin: 0 0 14px;
    font-family: "Great Vibes", cursive;
    font-weight: 400;
    font-size: 54px;
    line-height: 1;
    letter-spacing: 0.02em;
  }
  .promo__body {
    margin: 0;
    font-family: "Open Sans", sans-serif;
    font-weight: 600;
    font-size: 17.5px;
    line-height: 1.55;
  }
</style>
</head>
<body>
  <main class="banner">
    <svg class="banner__shapes" viewBox="0 0 950 425" preserveAspectRatio="none" aria-hidden="false">
      <defs>
        <linearGradient id="fabric-tone" x1="0" y1="1" x2="1" y2="0">
          <stop offset="0" stop-color="var(--photo-dark)"/>
          <stop offset="0.35" stop-color="var(--photo-mid)"/>
          <stop offset="0.7" stop-color="var(--photo-light)"/>
          <stop offset="1" stop-color="var(--photo-mid)"/>
        </linearGradient>
      </defs>
      <path class="wave-band" fill="var(--band-grey)"
        d="M0,213 C120,273 260,250 480,176 C650,120 820,116 950,126 L950,146 C820,134 650,138 480,192 C260,266 120,288 0,230 Z"/>
      <path class="hero-photo" role="img" aria-label="Close-up photograph of a silver metallic handbag with a gold zipper"
        fill="url(#fabric-tone)"
        d="M0,240 C120,300 260,276 480,202 C650,146 820,142 950,152 L950,425 L0,425 Z"/>
    </svg>

    <div class="brand">Mirelle</div>

    <section class="promo">
      <h1 class="promo__title">Lorem Ipsum Dolor</h1>
      <p class="promo__body">Lorem ipsum dolor sit amet, consectetur adipiscing elit,<br>sed do eiusmod tempor incididunt ut labore et</p>
    </section>
  </main>
</body>
</html>
```